Veltora Software Business Card Design

We are a new organization called Veltora. We are a software as a service provider. We deliver a project and program management solution via the internet, so everyone has the ability to work together and collaborate. Its an enterprise platform and we will focus on 50 plus employee company.

We have a website in place
www.veltora-demo.com

Use this as a start of producing the business card. The logo is there as well, but if you have a great and better solution...

Color scheme's could be inline with the website, but don't pin point on it. We can always change the website, logo, color scheme etc.

Target Market(s)

B2B, Projectmembers, projectmanagers, ICT, CTO, Marketing Managers

Industry/Entity Type

Software

Requirements
Must have
• Marten Kuyvelsma

Tel: +31 255 47 09 36
Mob: +31 6 927 15 062
marten@veltora-demo.com
Oostelingpad 84c
2184 KT Zuiderhaven

Www.veltora-demo.com
social media links

```html
<!DOCTYPE html>
<html lang="en">
<head>
<meta charset="utf-8">
<title>Veltora Business Card</title>
<link rel="stylesheet" href="https://fonts.googleapis.com/css2?family=Questrial&display=swap">
<style>
  :root {
    --backdrop: #3a2519;
    --lime-light: #bcd631;
    --lime: #a9c424;
    --lime-dark: #8ea61b;
    --ink-light: #eef3d6;
    --stripe: rgba(90, 110, 20, 0.35);
    --icon-blue: #3b6ea5;
    --rule: rgba(80, 100, 15, 0.45);
  }
  * { margin: 0; padding: 0; box-sizing: border-box; }
  html, body {
    width: 1200px; height: 900px; overflow: hidden;
    background: var(--backdrop);
    font-family: "Questrial", "Century Gothic", sans-serif;
  }
  .stage { position: relative; width: 1200px; height: 900px; }
  .card {
    position: absolute; left: 280px; width: 640px; height: 366px;
    border-radius: 26px; overflow: hidden;
    background: radial-gradient(ellipse at 35% 30%, var(--lime-light), var(--lime) 55%, var(--lime-dark));
    box-shadow: 0 10px 30px rgba(0,0,0,0.5);
    color: var(--ink-light);
  }
  .card--front { top: 70px; }
  .card--back { top: 464px; }
  .card__stripes { position: absolute; top: 0; right: 40px; }
  .front__brand {
    position: absolute; left: 44px; bottom: 48px;
    font-size: 108px; letter-spacing: 1px; line-height: 1;
    display: flex; align-items: center; gap: 18px;
  }
  .brand-square { width: 26px; height: 26px; background: var(--ink-light); }
  .back__brand {
    position: absolute; left: 34px; top: 40px;
    font-size: 36px; display: flex; align-items: center; gap: 10px;
  }
  .back__brand .brand-square { width: 12px; height: 12px; }
  .back__name { position: absolute; left: 60px; top: 150px; font-size: 20px; letter-spacing: 0.5px; }
  .contact {
    position: absolute; left: 100px; top: 205px;
    border-left: 2px solid var(--rule); padding-left: 22px;
    list-style: none; font-size: 13px; line-height: 22px;
  }
  .contact li, .social li { display: flex; align-items: center; gap: 12px; }
  .contact svg, .social svg { width: 13px; height: 13px; flex: none; }
  .social {
    position: absolute; right: 70px; top: 160px;
    border-left: 2px solid var(--rule); padding-left: 22px;
    list-style: none; font-size: 12px; line-height: 22px;
  }
  .social-square { width: 11px; height: 11px; background: var(--icon-blue); flex: none; }
  .address {
    position: absolute; left: 150px; bottom: 40px;
    font-size: 17px; display: flex; align-items: center; gap: 12px;
  }
  .address svg { width: 12px; height: 16px; }
</style>
</head>
<body>
<main class="stage">
  <section class="card card--front" aria-label="Card front">
    <svg class="card__stripes" width="220" height="120" viewBox="0 0 220 120">
      <g stroke="var(--stripe)" stroke-width="9">
        <line x1="20" y1="0" x2="20" y2="110"/>
        <line x1="95" y1="0" x2="95" y2="95"/>
        <line x1="170" y1="0" x2="170" y2="80"/>
      </g>
    </svg>
    <div class="front__brand"><span class="brand-square"></span>Veltora</div>
  </section>

  <section class="card card--back" aria-label="Card back">
    <svg class="card__stripes" width="220" height="120" viewBox="0 0 220 120">
      <g stroke="var(--stripe)" stroke-width="9">
        <line x1="20" y1="0" x2="20" y2="110"/>
        <line x1="95" y1="0" x2="95" y2="95"/>
        <line x1="170" y1="0" x2="170" y2="80"/>
      </g>
    </svg>
    <div class="back__brand"><span class="brand-square"></span>Veltora</div>
    <p class="back__name">Marten Kuyvelsma</p>
    <ul class="contact">
      <li><svg viewBox="0 0 16 16"><path fill="var(--icon-blue)" d="M3 1l3 0 1 4-2 1c1 2 3 4 5 5l1-2 4 1 0 3c0 1-1 2-2 2C7 15 1 9 1 3c0-1 1-2 2-2z"/></svg>+31 255 47 09 36</li>
      <li><svg viewBox="0 0 16 16"><rect x="4" y="1" width="8" height="14" rx="1.5" fill="none" stroke="var(--icon-blue)" stroke-width="1.8"/><circle cx="8" cy="12.3" r="1" fill="var(--icon-blue)"/></svg>+31 6 927 15 062</li>
      <li><svg viewBox="0 0 16 16"><text x="8" y="13" text-anchor="middle" font-size="15" fill="var(--icon-blue)" font-family="sans-serif">@</text></svg>marten@veltora-demo.com</li>
    </ul>
    <ul class="social">
      <li><span class="social-square"></span>Veltora</li>
      <li><span class="social-square"></span>VeltoraCOM</li>
      <li><svg viewBox="0 0 16 16"><path fill="var(--icon-blue)" d="M8 1l7 7h-2v7h-4v-4H7v4H3V8H1z"/></svg>Www.veltora-demo.com</li>
    </ul>
    <p class="address">
      <svg viewBox="0 0 12 16"><path fill="var(--icon-blue)" d="M6 0C2.7 0 0 2.6 0 5.8 0 10 6 16 6 16s6-6 6-10.2C12 2.6 9.3 0 6 0zm0 8a2.2 2.2 0 110-4.4A2.2 2.2 0 016 8z"/></svg>
      Oostelingpad 84c 2184 KT Zuiderhaven
    </p>
  </section>
</main>
</body>
</html>
```